Northern Terrain Published Photographer Website

I need a website to feature a home page slide show of 6 of my top photos then a few simple pages including; gallery, bio, social, checkout, services
Updates

Need extra days to review

Target Market(s)

photography

Industry/Entity Type

Photographer

Coding

Coded - Design and coding required

Number of Pages Required

5+ page

Colors

Designer to choose colors to be used in the design.

Requirements
Must have
• clean eye catching elegant trendy
Nice to have
• unique and creative from other photographer websites

```html
<!DOCTYPE html>
<html lang="en">
<head>
<meta charset="utf-8">
<title>Northern Terrain Photography</title>
<link href="https://fonts.googleapis.com/css2?family=Montserrat:wght@400;500;600;700&family=Open+Sans:wght@400&display=swap" rel="stylesheet">
<style>
  :root{
    --hero-bg:#f3f3f3;
    --ink:#1d1d1d;
    --muted:#9a9a9a;
    --rule:#cfcfcf;
    --dark:#262626;
    --footer:#2c2c2c;
    --light-text:#d6d6d6;
    --accent:#e8404f;
    --frame:#e4e4e4;
    --placeholder-a:#3a3a3a;
    --placeholder-b:#242424;
  }
  *{margin:0;padding:0;box-sizing:border-box}
  html,body{width:684px;height:1200px;overflow:hidden}
  body{position:relative;font-family:"Montserrat",sans-serif;background:var(--dark);color:var(--ink)}
  .hero{position:absolute;left:0;top:0;width:684px;height:292px;background:radial-gradient(ellipse at 50% 45%,#fafafa 0%,var(--hero-bg) 60%,#ececec 100%)}
  .brand{position:absolute;left:138px;top:9px;display:flex;align-items:center;gap:5px;font-size:11px;font-weight:500;letter-spacing:.2px;color:var(--ink)}
  .brand-dot{width:6px;height:6px;border-radius:50%;background:var(--ink)}
  .header-tools{position:absolute;left:522px;top:12px;display:flex;align-items:center;gap:6px}
  .header-tools .sep{width:1px;height:6px;background:var(--rule)}
  .hero-photo{position:absolute;left:254px;top:66px;width:166px;height:170px;background:linear-gradient(160deg,var(--placeholder-a),var(--placeholder-b))}
  .slide-count{position:absolute;left:133px;top:56px;writing-mode:vertical-rl;transform:rotate(180deg);font-size:4.5px;font-weight:600;letter-spacing:.5px;color:var(--ink)}
  .slide-count span{color:var(--muted);font-weight:400}
  .vline{position:absolute;width:1px;background:var(--rule)}
  .hline{position:absolute;height:1px;background:var(--rule)}
  .slide-num{position:absolute;left:143px;top:131px;font-size:23px;line-height:1;font-weight:700;color:#e6e6e6;letter-spacing:-1px}
  .slide-title{position:absolute;left:133px;top:143px;font-size:4.6px;font-weight:600;color:var(--ink);display:flex;align-items:center;gap:3px}
  .slide-title::before{content:"";width:5px;height:1px;background:var(--ink)}
  .slide-nav{position:absolute;left:133px;top:215px;font-size:4.4px;font-weight:600;line-height:9.5px}
  .slide-nav .next{color:var(--muted);font-weight:500}
  .social-rail{position:absolute;left:545px;font-size:4.4px;letter-spacing:1px;writing-mode:vertical-rl;transform:rotate(180deg);color:var(--muted)}
  .social-rail.active{color:var(--ink);font-weight:700}
  .scroll-mouse{position:absolute;left:338px;top:239px}
  .filters{position:absolute;top:326px;left:0;width:684px;font-size:5.6px;color:#bdbdbd;letter-spacing:.2px}
  .filters span{position:absolute}
  .filters .current{color:var(--accent)}
  .gallery{position:absolute;left:133.5px;top:352.5px;display:grid;grid-template-columns:repeat(4,96.3px);grid-template-rows:repeat(7,96px);column-gap:10.6px;row-gap:10.8px}
  .tile{width:100%;height:100%}
  .featured{background:var(--frame);padding:7px;position:relative}
  .featured .tile{position:relative}
  .featured-caption{position:absolute;left:0;right:0;top:42%;text-align:center;color:#fff;font-size:5.4px;letter-spacing:.1px}
  .featured-caption .mark{color:var(--accent)}
  .featured-caption .bar{display:block;width:11px;height:1px;background:var(--accent);margin:6px auto 6px}
  .featured-caption .handle{font-size:4.8px}
  .site-footer{position:absolute;left:0;top:1126px;width:684px;height:74px;background:var(--footer)}
  .footer-links{position:absolute;top:28px;left:0;width:684px;display:flex;justify-content:center;gap:14px;font-size:5.2px;letter-spacing:.8px;color:var(--light-text)}
  .footer-links span{display:flex;align-items:center;gap:3px}
  .footer-links i{width:3.5px;height:3.5px;background:var(--light-text);display:inline-block}
  .credit{position:absolute;top:42px;left:0;width:684px;text-align:center;font-family:"Open Sans",sans-serif;font-size:5px;color:var(--light-text)}
  .credit em{font-style:normal;color:var(--accent)}
</style>
</head>
<body>
  <section class="hero">
    <div class="brand"><span>Northern Terrain</span><span class="brand-dot"></span></div>
    <div class="header-tools">
      <svg width="7" height="7" viewBox="0 0 7 7"><circle cx="3" cy="3" r="2.2" fill="none" stroke="#1d1d1d" stroke-width=".7"/><line x1="4.6" y1="4.6" x2="6.5" y2="6.5" stroke="#1d1d1d" stroke-width=".7"/></svg>
      <span class="sep"></span>
      <svg width="9" height="6" viewBox="0 0 9 6"><line x1="0" y1=".5" x2="8" y2=".5" stroke="#1d1d1d" stroke-width=".7"/><line x1="0" y1="3" x2="6" y2="3" stroke="#1d1d1d" stroke-width=".7"/><line x1="0" y1="5.5" x2="4" y2="5.5" stroke="#1d1d1d" stroke-width=".7"/></svg>
    </div>

    <div class="slide-count">02 <span>/ 03</span></div>
    <div class="vline" style="left:135.5px;top:90px;height:14px"></div>
    <div class="hline" style="left:133px;top:120px;width:4px"></div>
    <div class="slide-num">02</div>
    <div class="slide-title">NORTHERN TERRAIN PHOTOGRAPHY</div>
    <div class="hline" style="left:133px;top:170px;width:4px"></div>
    <div class="vline" style="left:135.5px;top:187px;height:14px"></div>
    <div class="slide-nav"><div class="next">NEXT</div><div>PREVIOUS</div></div>

    <div class="hero-photo" role="img" aria-label="Featured slide photo: black camera on a white backdrop"></div>

    <div class="social-rail" style="top:56px">WORKNET</div>
    <div class="vline" style="left:548px;top:97px;height:21px"></div>
    <div class="social-rail active" style="top:129px">FRIENDBOOK</div>
    <div class="vline" style="left:548px;top:170px;height:21px"></div>
    <div class="social-rail" style="top:205px">CHIRPER</div>

    <svg class="scroll-mouse" width="8" height="12" viewBox="0 0 8 12"><rect x=".5" y=".5" width="7" height="11" rx="3.5" fill="none" stroke="#1d1d1d" stroke-width=".7"/><line x1="4" y1="3" x2="4" y2="5" stroke="#1d1d1d" stroke-width=".8"/></svg>
  </section>

  <nav class="filters">
    <span class="current" style="left:244px">• ALL</span>
    <span style="left:278px">NATURE</span>
    <span style="left:320px">LANDSCAPE</span>
    <span style="left:373px">SUNSETS</span>
    <span style="left:417px">SUNRISES</span>
    <span style="left:464px">WILDLIFE</span>
  </nav>

  <main class="gallery">
    <div class="tile" style="grid-column:1;grid-row:1;background:linear-gradient(#6b2a6e,#c04a6a 45%,#3a1a3f 80%,#1a0f1c)" role="img" aria-label="Desert tree silhouetted against a purple sunset"></div>
    <div class="tile" style="grid-column:2/4;grid-row:1;background:linear-gradient(#3a4466,#5b4a5e 30%,#a0502e 50%,#4d3a38 75%,#2a2a33)" role="img" aria-label="Canyon rim glowing at dusk"></div>
    <div class="tile" style="grid-column:4;grid-row:1;background:radial-gradient(circle at 45% 15%,#fff2b0,#e0a020 20%,#9a5a08 55%,#2a1a06)" role="img" aria-label="Golden sunrise over a pier with a heron"></div>

    <div class="tile" style="grid-column:1;grid-row:2;background:linear-gradient(#5a86c8,#c9d8ec 35%,#3d4a3a 55%,#dfe6ee 70%,#2a3340)" role="img" aria-label="Snowy river gorge under blue sky"></div>
    <div class="tile" style="grid-column:2;grid-row:2;background:linear-gradient(#7fb0e6,#a7c6ea 35%,#a06a50 50%,#b89878 75%,#8a7058)" role="img" aria-label="Bighorn sheep on desert scrubland"></div>
    <div class="featured" style="grid-column:3/5;grid-row:2/4">
      <div class="tile" style="background:linear-gradient(#5a4a9a,#8a62a8 35%,#c26a70 45%,#5e4c96 60%,#4a3a80)" role="img" aria-label="Glass sphere on a beach at twilight">
        <div class="featured-caption">NORTHERN TERRAIN PHOTOGRAPHY <span class="mark">•</span><span class="bar"></span><span class="handle">@NORTHERN.TERRAIN</span></div>
      </div>
    </div>

    <div class="tile" style="grid-column:1/3;grid-row:3/5;background:linear-gradient(#eef0f0,#d8cfc0 20%,#8a5a4a 35%,#9a5a44 55%,#2e5a4c 70%,#8a5440 90%)" role="img" aria-label="Horseshoe river bend through red canyon"></div>
    <div class="tile" style="grid-column:3;grid-row:4;background:linear-gradient(#1e2226,#3a3f44 40%,#8a4a20 62%,#3a2418 80%,#1a1614)" role="img" aria-label="Mesa under a stormy sunset"></div>
    <div class="tile" style="grid-column:4;grid-row:4;background:linear-gradient(#2f6ad0,#5a8ae0 30%,#b0502a 45%,#f0b040 55%,#8a6a5a 75%,#6a5a5a)" role="img" aria-label="Sunburst under a stone arch"></div>

    <div class="tile" style="grid-column:1;grid-row:5;background:linear-gradient(#8a3a08,#f0a020 35%,#d06010 55%,#3a1a06 70%,#c06010)" role="img" aria-label="Orange sunset over pier posts"></div>
    <div class="tile" style="grid-column:2/4;grid-row:5;background:linear-gradient(#7a88a8,#c8b8b0 30%,#5a6a9a 50%,#2e3a6a 70%,#2a2a3a)" role="img" aria-label="Snow capped mountain range"></div>
    <div class="tile" style="grid-column:4;grid-row:5;background:linear-gradient(#6a7080,#c0c6cc 25%,#6a8a40 50%,#8aa848 70%,#3a5a6a 90%)" role="img" aria-label="Green hills above a lake"></div>

    <div class="tile" style="grid-column:1;grid-row:6;background:linear-gradient(#c0501a,#3a6aa0 20%,#8a9ab0 45%,#a04a22 70%,#c0602a)" role="img" aria-label="Glass sphere under a stone arch"></div>
    <div class="tile" style="grid-column:2/4;grid-row:6/8;background:linear-gradient(#4ab0b0,#6ac0b8 20%,#e0a040 35%,#c07a30 55%,#d09040 65%,#3a9a9a 85%,#2a7070)" role="img" aria-label="Sandstone butte reflected in a lake"></div>
    <div class="tile" style="grid-column:4;grid-row:6;background:linear-gradient(#4a78c0,#e6eef6 30%,#2a3a2a 50%,#dfe6ee 65%,#1a2430)" role="img" aria-label="Snowy river gorge with evergreens"></div>

    <div class="tile" style="grid-column:1;grid-row:7;background:linear-gradient(#9aa0aa,#e6e8ea 35%,#6a7a8a 55%,#2a4a50 75%,#c09870)" role="img" aria-label="Lake among desert cliffs under clouds"></div>
    <div class="tile" style="grid-column:4;grid-row:7;background:linear-gradient(#e6eaee,#c0c8cc 25%,#5a7a3a 50%,#e0e0d8 70%,#4a6a2a)" role="img" aria-label="Waterfall below an arched bridge in autumn"></div>
  </main>

  <footer class="site-footer">
    <div class="footer-links">
      <span><i></i>FRIENDBOOK</span>
      <span><i></i>CHIRPER</span>
      <span><i></i>SNAPGRAM</span>
      <span><i></i>SHOTBOARD</span>
    </div>
    <p class="credit">Created by: <em>Lena Voss</em> ©2019. All Rights Reserved.</p>
  </footer>
</body>
</html>
```